Business card for home developer

Name, email, phone #, logo, address, lic # and slogan.
Slogan to say something like, "Leader in quality neighborhood communities" maybe? The last one said "A sept above the rest". Some thing saying we are above the other people.
The card can be two sided?
Home buyers
Business

```html
<!DOCTYPE html>
<html lang="en">
<head>
<meta charset="utf-8">
<title>Summit Homes — Business Card</title>
<link href="https://fonts.googleapis.com/css2?family=Roboto:wght@400;900&family=Dancing+Script:wght@500&family=Kalam:wght@700&display=swap" rel="stylesheet">
<style>
  :root {
    --backdrop: #6e4483;
    --brick-light: #c9775a;
    --brick-mid: #b15e43;
    --brick-dark: #8f4634;
    --card-white: #ffffff;
    --band-edge: #f2e23a;
    --brand-navy: #2d3f7f;
    --slogan-violet: #4a3fa0;
    --ink: #1e1e1e;
  }
  * { margin: 0; padding: 0; box-sizing: border-box; }
  html, body { width: 1200px; height: 666px; overflow: hidden; }
  body { background: var(--backdrop); position: relative; font-family: "Roboto", Arial, sans-serif; }

  .card {
    position: absolute;
    width: 562px;
    height: 350px;
    overflow: hidden;
  }
  .brick-surface {
    position: absolute;
    inset: 0;
    background: linear-gradient(135deg, var(--brick-light), var(--brick-mid) 50%, var(--brick-dark));
  }

  /* Front */
  .card-front {
    left: 366px;
    top: 332px;
    transform: translate(-50%, -50%) rotate(-26.5deg);
  }
  .front-band {
    position: absolute;
    left: -4px;
    right: -4px;
    top: 148px;
    height: 124px;
    background: var(--card-white);
    border: 3px solid var(--band-edge);
    display: flex;
    flex-direction: column;
    align-items: center;
    justify-content: center;
  }

  .brand {
    display: flex;
    align-items: center;
    gap: 8px;
  }
  .brand-name {
    font-weight: 900;
    font-size: 34px;
    color: var(--brand-navy);
    letter-spacing: 0.5px;
    text-transform: uppercase;
  }
  .brand-dot {
    width: 22px;
    height: 22px;
    border-radius: 50%;
    background: var(--brand-navy);
  }
  .slogan {
    font-family: "Dancing Script", cursive;
    font-size: 24px;
    color: var(--slogan-violet);
    margin-top: 4px;
  }

  /* Back */
  .card-back {
    left: 583px;
    top: 192px;
    width: 562px;
    height: 348px;
  }
  .back-arch {
    position: absolute;
    inset: 0;
  }
  .back-brand {
    position: absolute;
    left: 0;
    width: 562px;
    top: 62px;
    display: flex;
    flex-direction: column;
    align-items: center;
    padding-left: 0;
  }
  .holder-name {
    position: absolute;
    left: 66px;
    top: 222px;
    font-family: Arial, "Roboto", sans-serif;
    font-size: 25px;
    color: var(--ink);
  }
  .contact-list {
    position: absolute;
    left: 352px;
    top: 172px;
    list-style: none;
    font-family: "Kalam", cursive;
    font-size: 24px;
    line-height: 38px;
    color: var(--ink);
  }
</style>
</head>
<body>

  <section class="card card-front" aria-label="Card front">
    <div class="brick-surface" role="img" aria-label="Red brick wall texture"></div>
    <div class="front-band">
      <div class="brand">
        <span class="brand-name">Summit Homes</span>
        <span class="brand-dot"></span>
      </div>
      <p class="slogan">A Step above the rest</p>
    </div>
  </section>

  <section class="card card-back" aria-label="Card back">
    <div class="brick-surface" role="img" aria-label="Red brick wall texture"></div>
    <svg class="back-arch" width="562" height="348" viewBox="0 0 562 348" aria-hidden="true">
      <path d="M14 348 L14 330 A267 330 0 0 1 548 330 L548 348 Z" fill="var(--card-white)"/>
    </svg>
    <div class="back-brand">
      <div class="brand">
        <span class="brand-name">Summit Homes</span>
        <span class="brand-dot"></span>
      </div>
      <p class="slogan">A Step above the rest</p>
    </div>
    <p class="holder-name">Your Name</p>
    <ul class="contact-list">
      <li>Address</li>
      <li>Phone #</li>
      <li>E-mail</li>
      <li>lic #</li>
    </ul>
  </section>

</body>
</html>
```